Website design for commercial and residential security company

we're looking to see some new designs for an established company with no website.

homepage and one inner page

here is a link to the homepage content, sitemap, logo and more.
https://files.brontavel.net/share/7QxmPzLrTw2vNkdJhYcsa9eFgbUoiVwRn?view=open

call to action should be Request A Quote

if you have any questions please send them to us asap

thank you

1 page

Sans Serif

```html
<!DOCTYPE html>
<html lang="en">
<head>
<meta charset="utf-8">
<title>Keystone Guard – Commercial &amp; Residential Security</title>
<link href="https://fonts.googleapis.com/css2?family=Oswald:wght@400;500&family=Lato:wght@400;700&display=swap" rel="stylesheet">
<style>
:root{
  --gold:#cfab36;
  --gold-soft:#d7b54a;
  --ink:#222326;
  --muted:#8b8b8b;
  --light:#f5f5f5;
  --line:#e3e3e3;
  --footer:#3d3e42;
  --white:#ffffff;
}
*{margin:0;padding:0;box-sizing:border-box}
html,body{width:1200px;height:3662px;overflow:hidden}
body{position:relative;background:var(--white);font-family:'Lato',sans-serif;color:var(--ink)}
.abs{position:absolute}
.display{font-family:'Oswald',sans-serif;font-weight:400;letter-spacing:.5px}
.btn{position:absolute;background:var(--gold);color:var(--white);font-size:14px;display:flex;align-items:center;justify-content:center}
.muted{color:var(--muted)}

/* top strip + header */
.top-strip{left:0;top:0;width:1200px;height:21px;background:#bdbdbd}
.site-header{left:0;top:21px;width:1200px;height:76px;background:var(--white);border-bottom:1px solid var(--line)}
.brand{position:absolute;font-family:'Oswald',sans-serif;font-weight:500;color:var(--gold);font-size:22px;letter-spacing:1px}
.header-contact{top:14px;font-size:12px;color:var(--muted);display:flex;align-items:center;gap:6px}
.header-contact .ring{width:18px;height:18px;border:1px solid #bbb;border-radius:50%;display:flex;align-items:center;justify-content:center}
.main-nav{top:47px;font-family:'Oswald',sans-serif;font-size:14px;color:var(--ink)}
.main-nav.active{color:var(--gold)}

/* hero */
.hero{left:0;top:97px;width:1200px;height:479px;background:linear-gradient(100deg,#a9a9a7 0%,#c4c4c2 45%,#b8b8b6 100%)}
.hero-title{left:183px;top:88px;font-size:50px;line-height:57px;color:var(--white)}
.hero-text{left:183px;top:230px;width:400px;font-size:13.5px;line-height:24px;color:var(--white)}

/* about */
.about-art{left:213px;top:650px;width:398px;height:392px;border-radius:50%;background:radial-gradient(circle,#f4e2b4 0%,#e6eef3 55%,#ffffff 75%)}
.section-title{font-size:20px;color:var(--ink)}
.lead{font-size:16.5px;line-height:25px;color:var(--muted)}
.body-text{font-size:12.5px;line-height:25px;color:var(--muted)}

/* services */
.services{left:0;top:1123px;width:1200px;height:644px;background:var(--light)}
.bullet{font-size:13px;display:flex;align-items:center;gap:10px}
.bullet i{width:5px;height:5px;border-radius:50%;background:var(--gold);display:block}
.service-card{position:absolute;top:246px;width:263px;height:313px;background:var(--white);padding:52px 30px 0}
.service-card.featured{background:var(--gold);box-shadow:0 8px 20px rgba(0,0,0,.12)}
.service-card .icon{width:52px;height:52px;border:2px solid var(--ink);border-radius:8px}
.service-card.featured .icon{border-color:var(--white)}
.service-card h3{font-family:'Oswald',sans-serif;font-weight:400;font-size:19px;color:var(--gold);margin-top:38px;letter-spacing:.5px}
.service-card.featured h3,.service-card.featured p{color:var(--white)}
.service-card p{font-size:12.5px;line-height:23px;color:var(--muted);margin-top:12px}

/* blog */
.blog-photo{position:absolute;top:1973px;width:406px;height:231px}
.post-meta{font-size:10px;color:var(--muted)}
.post-title{font-size:14.5px;line-height:26px;color:var(--ink);width:400px}
.post-text{font-size:12.5px;line-height:25px;color:var(--muted);width:400px}

/* contact */
.contact-band{left:0;top:2537px;width:1200px;height:354px;background:linear-gradient(90deg,#5a4c3c 0%,#4a4d55 45%,#55585f 100%)}
.contact-line{color:var(--white);font-size:14px;line-height:20px;display:flex;gap:10px;letter-spacing:.5px}
.social{position:absolute;width:27px;height:27px;border:1px solid var(--white);border-radius:50%}

/* testimonials */
.testimonial{position:absolute;top:3100px;width:263px;height:170px;background:var(--white);box-shadow:0 6px 22px rgba(0,0,0,.08);padding:46px 20px 0}
.testimonial.featured{background:var(--gold);box-shadow:0 10px 26px rgba(207,171,54,.35)}
.testimonial p{font-size:11.5px;line-height:19px;color:var(--muted)}
.testimonial.featured p,.testimonial.featured .who{color:var(--white)}
.testimonial .who{position:absolute;left:20px;top:124px;font-size:12px;color:var(--ink);line-height:17px}
.testimonial .who small{font-size:10px;display:block}
.testimonial .stars{position:absolute;right:28px;top:126px;font-size:11px;color:#f08a1c;letter-spacing:1px}
.testimonial.featured .stars{color:var(--white)}
.avatar{position:absolute;width:54px;height:54px;border-radius:50%;background:linear-gradient(135deg,#8a7a6a,#4a4a4a);border:3px solid var(--white)}
.arrow{position:absolute;width:18px;height:18px;border-radius:50%;display:flex;align-items:center;justify-content:center}

/* footer */
.site-footer{left:0;top:3351px;width:1200px;height:311px;background:var(--footer)}
.footer-link{position:absolute;font-family:'Oswald',sans-serif;font-size:14px;color:var(--white)}
.footer-social{position:absolute;width:27px;height:27px;border:1px solid var(--white);border-radius:50%}
</style>
</head>
<body>

<div class="abs top-strip"></div>
<header class="abs site-header">
  <div class="brand" style="left:183px;top:22px">KEYSTONE GUARD</div>
  <div class="abs header-contact" style="left:712px">
    <span class="ring"><svg width="9" height="9" viewBox="0 0 24 24"><path d="M6 2l4 4-2 3a12 12 0 0 0 7 7l3-2 4 4-3 4C10 22 2 14 2 5z" fill="#999"/></svg></span>(555) 014-2287
  </div>
  <div class="abs header-contact" style="left:845px">
    <span class="ring"><svg width="10" height="8" viewBox="0 0 20 14"><rect x="1" y="1" width="18" height="12" fill="none" stroke="#999" stroke-width="2"/><path d="M1 1l9 7 9-7" fill="none" stroke="#999" stroke-width="2"/></svg></span>hello@keystoneguard.com
  </div>
  <nav>
    <span class="abs main-nav active" style="left:637px">Home</span>
    <span class="abs main-nav" style="left:709px">About Us</span>
    <span class="abs main-nav" style="left:799px">Our Services</span>
    <span class="abs main-nav" style="left:909px">Blog</span>
    <span class="abs main-nav" style="left:973px">Contact</span>
  </nav>
</header>

<section class="abs hero" role="img" aria-label="Security camera mounted on a grey corrugated wall">
  <h1 class="abs display hero-title">Secure The Things You<br>Care About.</h1>
  <p class="abs hero-text">Lorem ipsum dolor sit amet, consectetur adipiscing elit, sed do eiusmod tempor incididunt ut labore et dolore magna aliqua. Quis ipsum suspendisse ultrices gravida.</p>
  <a class="btn" style="left:183px;top:338px;width:125px;height:44px">Read More</a>
</section>

<section>
  <div class="abs about-art" role="img" aria-label="Illustration of a house connected to a camera, alarm, keypad and control panel"></div>
  <h2 class="abs display section-title" style="left:660px;top:680px">About Us</h2>
  <p class="abs lead" style="left:660px;top:732px;width:340px">Sed do eiusmod tempor incididunt ut labore et dolore magna aliqua</p>
  <p class="abs body-text" style="left:660px;top:791px;width:345px">Lorem ipsum dolor sit amet, consectetur adipiscing elit, sed do eiusmod tempor incididunt ut labore et dolore magna aliqua. Ut enim ad minim veniam.</p>
  <p class="abs body-text" style="left:660px;top:889px;width:345px">Quis nostrud exercitation ullamco laboris nisi ut aliquip ex ea commodo consequat.Duis aute irure dolor in reprehenderit in voluptate.</p>
  <a class="btn" style="left:660px;top:1001px;width:128px;height:45px">Learn More</a>
</section>

<section class="abs services">
  <h2 class="abs display section-title" style="left:183px;top:54px">Our Services</h2>
  <p class="abs lead" style="left:183px;top:107px;width:340px">Quis nostrud exercitation ullamco laboris nisi ut aliquip ex ea commodo consequat.</p>
  <p class="abs body-text" style="left:611px;top:52px;width:340px">Lorem ipsum dolor sit amet, consectetur adipisicing elit, sed do eiusmod tempor incididunt ut labore et dolore magna aliqua.</p>
  <div class="abs bullet" style="left:611px;top:150px"><i></i>Commercial Security</div>
  <div class="abs bullet muted" style="left:611px;top:173px"><i style="background:#bbb"></i>Residential Security</div>

  <div class="service-card featured" style="left:183px">
    <div class="icon" role="img" aria-label="CCTV icon"></div>
    <h3>CCTV</h3>
    <p>Lorem ipsum dolor sit amet, consectetur adipiscing elit, sed do eiusmod tempor incididunt ut labore et dolore.</p>
  </div>
  <div class="service-card" style="left:468px">
    <div class="icon" role="img" aria-label="Access control icon"></div>
    <h3>Access Control</h3>
    <p>Sed do eiusmod tempor incididunt ut labore et dolore magna aliqua. Quis ipsum suspendisse ultrices gravida.</p>
  </div>
  <div class="service-card" style="left:754px">
    <div class="icon" role="img" aria-label="Alarm system icon"></div>
    <h3>Alarm System</h3>
    <p>Lorem ipsum dolor sit amet, consectetur adipiscing elit, sed do eiusmod tempor incididunt ut labore et dolore magna.</p>
  </div>
  <div class="service-card" style="left:1039px">
    <div class="icon" role="img" aria-label="Audio systems icon"></div>
    <h3 style="white-space:nowrap">Audio Systems</h3>
    <p style="white-space:nowrap">Ut enim ad minim veniam,<br>nostrud exercitation ullamco<br>laboris nisi ut aliquip ex ea<br>commodo consequat.</p>
  </div>
</section>

<section>
  <h2 class="abs display section-title" style="left:183px;top:1822px">Blog</h2>
  <p class="abs lead" style="left:183px;top:1875px;width:330px;font-size:16px;letter-spacing:.8px">Sed do eiusmod tempor incididunt ut labore et dolore magna aliqua</p>
  <p class="abs body-text" style="left:611px;top:1821px;width:340px;letter-spacing:.8px">Lorem ipsum dolor sit amet, consectetur adipiscing elit, sed do eiusmod tempor incididunt ut labore et dolore magna aliqua. Ut enim ad minim veniam.</p>

  <div class="blog-photo" style="left:183px;background:linear-gradient(135deg,#3a3a3a,#8a8a8a 60%,#4d4d4d)" role="img" aria-label="Wall-mounted security camera on a dark concrete wall"></div>
  <div class="blog-photo" style="left:611px;background:linear-gradient(135deg,#2f6c9c,#5d98c4 55%,#8aa88a)" role="img" aria-label="Dome security camera on a pole in front of a glass building"></div>

  <p class="abs post-meta" style="left:189px;top:2212px">Posted on: 20.03.2021</p>
  <h3 class="abs post-title" style="left:189px;top:2232px;font-weight:400">Lorem ipsum dolor sit amet, consectetur adipiscing elit, sed do eiusmod tempor incididunt ut labore.</h3>
  <p class="abs post-text" style="left:189px;top:2296px">Lorem ipsum dolor sit amet, consectetur adipiscing elit, sed do eiusmod tempor incididunt ut labore et dolore magna aliqua. Ut enim ad minim veniam, quis nostrud exercitation ullamco laboris nisi ut aliquip ex ea commodo consequat.</p>

  <p class="abs post-meta" style="left:611px;top:2212px">Posted on: 20.03.2021</p>
  <h3 class="abs post-title" style="left:611px;top:2232px;font-weight:400">Lorem ipsum dolor sit amet, consectetur adipiscing elit, sed do eiusmod tempor incididunt ut labore.</h3>
  <p class="abs post-text" style="left:611px;top:2296px">Lorem ipsum dolor sit amet, consectetur adipiscing elit, sed do eiusmod tempor incididunt ut labore et dolore magna aliqua. Ut enim ad minim veniam, quis nostrud exercitation ullamco laboris nisi ut aliquip ex ea commodo consequat.</p>

  <a class="btn" style="left:537px;top:2438px;width:126px;height:45px">View More</a>
</section>

<section class="abs contact-band" role="img" aria-label="Dome security camera in front of blurred city buildings">
  <h2 class="abs display section-title" style="left:243px;top:72px;color:var(--white)">Contact</h2>
  <div class="abs contact-line" style="left:243px;top:130px">
    <svg width="12" height="16" viewBox="0 0 12 16" style="margin-top:3px"><path d="M6 1a5 5 0 0 0-5 5c0 4 5 9 5 9s5-5 5-9a5 5 0 0 0-5-5z" fill="none" stroke="#fff" stroke-width="1.4"/><circle cx="6" cy="6" r="1.8" fill="#fff"/></svg>
    <span>Lorem ipsum,dolor sit amet,<br>21548 adipiscing elit,</span>
  </div>
  <div class="abs contact-line" style="left:243px;top:178px">
    <svg width="12" height="12" viewBox="0 0 24 24" style="margin-top:4px"><path d="M6 2l4 4-2 3a12 12 0 0 0 7 7l3-2 4 4-3 4C10 22 2 14 2 5z" fill="#fff"/></svg>
    <span>(555) 014-2287</span>
  </div>
  <div class="abs contact-line" style="left:243px;top:206px">
    <svg width="12" height="10" viewBox="0 0 20 14" style="margin-top:5px"><rect x="1" y="1" width="18" height="12" fill="none" stroke="#fff" stroke-width="2"/><path d="M1 1l9 7 9-7" fill="none" stroke="#fff" stroke-width="2"/></svg>
    <span>hello@keystoneguard.com</span>
  </div>
  <span class="social" style="left:248px;top:251px" aria-label="Social profile"></span>
  <span class="social" style="left:289px;top:251px" aria-label="Social profile"></span>
  <span class="social" style="left:331px;top:251px" aria-label="Social profile"></span>
</section>

<section>
  <h2 class="abs display section-title" style="left:0;top:2956px;width:1200px;text-align:center">Testimonial</h2>
  <p class="abs lead" style="left:0;top:3002px;width:1200px;text-align:center;font-size:15.5px">We care About Our Customers Experience too</p>

  <span class="arrow" style="left:135px;top:3176px;border:1px solid #ccc"><svg width="6" height="8" viewBox="0 0 6 8"><path d="M5 1L2 4l3 3" fill="none" stroke="#aaa" stroke-width="1.2"/></svg></span>
  <span class="arrow" style="left:1046px;top:3176px;background:var(--gold)"><svg width="6" height="8" viewBox="0 0 6 8"><path d="M1 1l3 3-3 3" fill="none" stroke="#fff" stroke-width="1.2"/></svg></span>

  <div class="testimonial featured" style="left:183px">
    <p>Lorem ipsum dolor sit amet, consectetur adipiscing elit, sed do eiusmod tempor incididunt ut labore et dolore.</p>
    <div class="who">John Doe<small>Funder of Lorem</small></div>
    <div class="stars">★★★★☆</div>
  </div>
  <div class="testimonial" style="left:468px">
    <p>Lorem ipsum dolor sit amet, consectetur adipiscing elit, sed do eiusmod tempor incididunt ut labore et dolore.</p>
    <div class="who">John Doe<small>Funder of Lorem</small></div>
    <div class="stars">★★★★☆</div>
  </div>
  <div class="testimonial" style="left:754px">
    <p>Lorem ipsum dolor sit amet, consectetur adipiscing elit, sed do eiusmod tempor incididunt ut labore et dolore.</p>
    <div class="who">John Doe<small>Funder of Lorem</small></div>
    <div class="stars">★★★★☆</div>
  </div>
  <div class="avatar" style="left:205px;top:3071px" role="img" aria-label="Customer portrait"></div>
  <div class="avatar" style="left:489px;top:3071px" role="img" aria-label="Customer portrait"></div>
  <div class="avatar" style="left:773px;top:3071px" role="img" aria-label="Customer portrait"></div>
</section>

<footer class="abs site-footer">
  <div class="brand" style="left:193px;top:88px;font-size:28px">KEYSTONE GUARD</div>
  <span class="footer-social" style="left:198px;top:163px" aria-label="Social profile"></span>
  <span class="footer-social" style="left:240px;top:163px" aria-label="Social profile"></span>
  <span class="footer-social" style="left:282px;top:163px" aria-label="Social profile"></span>

  <span class="footer-link" style="left:424px;top:84px">Home</span>
  <span class="footer-link" style="left:533px;top:84px">Blog</span>
  <span class="footer-link" style="left:638px;top:84px">FAQ</span>
  <span class="footer-link" style="left:424px;top:138px">About Us</span>
  <span class="footer-link" style="left:533px;top:138px">Contact</span>
  <span class="footer-link" style="left:638px;top:138px">Social</span>
  <span class="footer-link" style="left:424px;top:192px">Our Service</span>
  <span class="footer-link" style="left:533px;top:192px">Testimonial</span>

  <span class="footer-link" style="left:754px;top:84px">Subscribe Our Newsletter</span>
  <div class="abs" style="left:754px;top:130px;width:199px;height:30px;background:var(--white);font-size:10px;color:#999;padding:9px 13px">Enter Your Email</div>
  <div class="abs" style="left:954px;top:130px;width:34px;height:30px;background:var(--gold);display:flex;align-items:center;justify-content:center">
    <svg width="12" height="12" viewBox="0 0 24 24"><path d="M2 12l20-9-6 19-4-8z" fill="none" stroke="#fff" stroke-width="2"/></svg>
  </div>

  <div class="abs" style="left:183px;top:256px;width:834px;height:1px;background:#5a5b60"></div>
  <span class="abs" style="left:183px;top:270px;font-family:'Oswald',sans-serif;font-size:10.5px;color:var(--white)">© Copyright @KeystoneGuard | All Rights Reserved</span>
  <span class="abs" style="left:868px;top:270px;width:149px;text-align:right;font-family:'Oswald',sans-serif;font-size:10.5px;color:var(--white)">Privacy &amp; Policy | Trams &amp; Condition</span>
</footer>

</body>
</html>
```